Vell Partners Building Business Cards

We need a business card that reflects our business as "Solar Experts" in San Diego. Browse our website www.vellpartners.example our License needs to be displayed as "CSLB# 4718392" our phone number is (619) 555-0147

Save thousands on your electric bills and increase the value of your home while helping to protect the environment. Our solar installation experts will help you design the system that's right for you, using only the highest quality equipment that will look great and give you ideal performance. Our goal is to make you energy independent, and get your electric bill to 0.

Tobias Wrenfield
(619) 555-0147
tobias@vellpartners.example

Target Market(s)

Home owners in san diego looking for solar

Industry/Entity Type

Solar Energy

Contact Information for Business Card

Tobias Wrenfield
(619) 555-0147
tobias@vellpartners.example

Font styles to use
Other font styles liked:
• Use our logo font

Requirements
Must have
• License needs to be displayed as "CSLB# 4718392" our phone number is (619) 555-0147
Nice to have
• Real images of rooftop home solar in san diego
Should not have
• our business address

```html
<!DOCTYPE html>
<html lang="en">
<head>
<meta charset="utf-8">
<title>Vell Partners Building – Business Card</title>
<link rel="stylesheet" href="https://fonts.googleapis.com/css2?family=Open+Sans:wght@400;600;700&display=swap">
<style>
  :root {
    --stage: #000000;
    --card-front: #1f3f7b;
    --card-back: #231f1e;
    --brand-gold: #f5b21b;
    --brand-blue: #214a91;
    --ink-light: #ffffff;
    --sans: "Open Sans", Arial, sans-serif;
  }
  * { margin: 0; padding: 0; box-sizing: border-box; }
  html, body { width: 1200px; height: 900px; overflow: hidden; background: var(--stage); }
  .stage { position: relative; width: 1200px; height: 900px; font-family: var(--sans); }

  .card { position: absolute; top: 275px; width: 477px; height: 293px; overflow: hidden; }
  .card-front { left: 116px; background: var(--card-front); border-radius: 0 48px 0 48px; }
  .card-back { left: 622px; background: var(--card-back); border-radius: 48px 0 48px 0; }

  .wordmark {
    position: absolute; display: flex; align-items: center; gap: 12px;
    font-family: var(--sans); font-weight: 700; font-size: 31px; letter-spacing: -0.3px; white-space: nowrap;
  }
  .wordmark .dot { width: 18px; height: 18px; border-radius: 50%; background: var(--brand-gold); flex: none; }
  .card-front .wordmark { left: 62px; top: 58px; color: var(--ink-light); }
  .card-back .wordmark { left: 48px; top: 124px; color: var(--brand-blue); }

  .holder { position: absolute; left: 29px; top: 161px; width: 448px; display: flex; align-items: center; gap: 16px; }
  .holder-name { color: var(--brand-gold); font-weight: 700; font-size: 16px; text-transform: uppercase; white-space: nowrap; }
  .holder-rule { flex: 1; height: 1px; background: var(--ink-light); }

  .contact { position: absolute; right: 25px; top: 202px; text-align: right; color: var(--ink-light); font-size: 13px; line-height: 18px; }
  .contact-line { display: flex; justify-content: flex-end; align-items: center; gap: 6px; }
  .contact-line svg { width: 10px; height: 10px; fill: var(--brand-gold); }
  .license { margin-top: 11px; padding-right: 0; }
  .license-label { color: var(--brand-gold); font-weight: 700; }
</style>
</head>
<body>
<main class="stage">
  <section class="card card-front" aria-label="Business card front">
    <div class="wordmark"><span class="dot"></span>Vell Partners Building</div>
    <div class="holder">
      <span class="holder-name">Tobias Wrenfield</span>
      <span class="holder-rule"></span>
    </div>
    <div class="contact">
      <div class="contact-line">(619) 555-0147
        <svg viewBox="0 0 10 10" aria-hidden="true"><path d="M2 0.5 L3.6 2.6 L2.8 3.6 C3.4 5 4.9 6.6 6.4 7.2 L7.4 6.4 L9.5 8 L8.4 9.5 C4.5 9.2 0.8 5.5 0.5 1.6 Z"/></svg>
      </div>
      <div class="contact-line">tobias@vellpartners.example
        <svg viewBox="0 0 10 10" aria-hidden="true"><path d="M0.5 2 H9.5 V8 H0.5 Z M0.8 2.3 L5 5.4 L9.2 2.3" stroke="#1f3f7b" stroke-width="0.8"/></svg>
      </div>
      <div class="contact-line license"><span><span class="license-label">LICENSE:</span> CSLB# 4718392</span></div>
    </div>
  </section>

  <section class="card card-back" aria-label="Business card back">
    <div class="wordmark"><span class="dot"></span>Vell Partners Building</div>
  </section>
</main>
</body>
</html>
```